Anzeigengestaltung für KURSHEFT WERK & GEFÜGE 2016/2017 –  BADEN-WÜRTTEMBERG
Anzeigengestaltung für KURSHEFT WERK & GEFÜGE 2016/2017 – BADEN-WÜRTTEMBERG
Zielgruppe
Wir sind ein mittelständischer Versicherungsmakler in Stuttgart und möchten eine halbe Seite in dem KURSHEFT WERK & GEFÜGE 2016/2017 – BADEN-WÜRTTEMBERG anbieten. Hier Informationen dazu:
'Jährlich drucken wir einen umfassenden Seminarkalender für unsere Mitglieds-unternehmen. Wir sind insgesamt vier Dienstleister der Weiterbildung für Verbands-mitgliedsbetriebe aus den Bereichen Hoch-, Straßen- und Tiefbau, Zimmerer- und Holzbau, Trockenbau, dem Stuckateurhandwerk und für Schreinerbetriebe.
 Lernwerkgesellschaft der Oberländischen Fachgewerke mbH
 Qualifizierungskreis der Rheintaler Handwerkerschaft GmbH
 Dienstkontor der Gewerkeverbände mbH Nordwald
 Hilfswerk-GmbH der Fachgewerke Kaiserstuhl
Als Partner unserer Betriebe möchten wir Ihnen diese Werbefläche für Ihre Kunden
anbieten. Das Seminarprogramm ist bei unseren Betrieben seit Jahren eingeführt und ein
wichtiges Druckwerk. Das geplante Programm 2016/2017 umfasst ca. 200 Seminare
im Zeitraum September 2016 bis Juli 2017.
Der Seminarkalender wird all unseren Mitgliedsbetrieben, insgesamt 2.500 Betriebe,
im August/September 2016 per Post zugesandt. Das Verteilungsgebiet erstreckt sich
über Württemberg und Südbaden. In diesem Jahr, aufgrund einer gestiegenen Nachfrage
über das Verteilungsgebiet hinaus, in einer erhöhten Auflage von ca. 6.000 Stück.
Die Unternehmen nutzen die Broschüre über ein Jahr zur Planung ihrer Weiterbildung.
Diese attraktive Werbeplattform bieten wir Ihnen an! Gerne nehmen wir Ihre Werbung
mit in das Programm auf.'
Wir wollen durch die Anzeige neue Kunden werben speziell in der o. g. Branche (Bau), da wir darauf spezialisiert sind.
Aufgabenstellung
Anzeige soll modern sein, einladend. Es soll rüberkommen, dass wir der perfekte Versicherungsmakler für die Branche sind und innovative und spezielle Lösungen anbieten können.
Da hier ein Versicherer (die PLR) sehr auffällig und groß wirbt (mit Gelb und schwarz) sollte unsere Anzeige schon auch auffallen.
Unsere Kontaktdaten sollen erscheinen und eventuell ein Ansprechpartner (dies je nach Empfehlung Ihrerseits).
Puristisch aber auffallend. Interessant und Neugierig soll die Anzeige sein. Unser Leitspruch: Zuverlässig. Kompetent. Vertrauensvoll. Wir sind Ihr Partner!
Unsere Farben:
Dunkler Blauton in RGB: 48 / 72 / 162, der helle Blauton in RGB: 44 / 152 / 224
Hier die Informationen zur Anzeige die uns vorliegen:
Anzeigenformat:
Breite 210 mm x Höhe 140mm (Beschnitt rechts und links ohne Schnittmarken)
Datenformat: Breite 216 x Höhe 140 mm
Nur digitale Vorlagen einsenden.
1. Anzeigen, druckfähige / reprofähige PDF-Daten
Schriften und Bilddaten vollständig eingebettet, "PDF-X3-Standard"
Generell keine Schnittmarken o. ä.
2. Produktabbildung, druckfähige/ reprofähige Daten, TIF- oder JPG-Bilddaten
Halbtonbilder mindestens 300 dpi, Strichbilder 1200 dpi
Frist zur Einsendung ist der 06.05.2016!

```html
<!DOCTYPE html>
<html lang="de">
<head>
<meta charset="utf-8">
<title>Anzeige – Brandt Versicherungsmakler</title>
<link href="https://fonts.googleapis.com/css2?family=Open+Sans:ital,wght@0,400;0,700;0,800;1,700&display=swap" rel="stylesheet">
<style>
  :root{
    --blue-dark:#3048a2;
    --blue-light:#2c98e0;
    --ribbon-gold:#a88a3c;
    --ribbon-green:#98a042;
    --ribbon-steel:#7f97ac;
    --text-dark:#222;
    --page-bg:#e4e4e4;
  }
  html,body{margin:0;padding:0;width:1200px;height:1200px;overflow:hidden;background:var(--page-bg);}
  body{font-family:"Open Sans",Arial,sans-serif;}
  .ad{position:absolute;left:50px;top:234px;width:1100px;height:732px;background:#fff;overflow:hidden;box-shadow:0 4px 18px rgba(0,0,0,.18);}
  .ad-graphics{position:absolute;left:0;top:0;width:1100px;height:732px;}
  .ribbon-label{font-family:"Open Sans",Arial,sans-serif;font-size:19px;fill:#fff;letter-spacing:.5px;}
  .photo{position:absolute;left:0;top:80px;width:440px;height:652px;
    clip-path:polygon(0 0,165px 0,165px 175px,440px 175px,440px 100%,0 100%);
    background:linear-gradient(180deg,#d9c86a 0%,#c9b7a4 20%,#9aa0a8 45%,#3b4f96 75%,#2d3f86 100%);}
  .headline{position:absolute;left:180px;top:40px;margin:0;font-weight:800;line-height:1;text-transform:uppercase;}
  .headline span{display:block;}
  .headline .dark{color:var(--blue-dark);font-size:36px;}
  .headline .light{color:var(--blue-light);font-size:54px;margin-left:55px;}
  .headline .dark.indent{margin-left:55px;margin-top:4px;}
  .headline .l1{margin-top:2px;}
  .brand{position:absolute;left:685px;top:52px;display:flex;align-items:flex-start;gap:16px;}
  .brand-mark{width:44px;height:44px;background:var(--blue-light);margin-top:10px;}
  .brand-name{font-size:20px;color:var(--text-dark);line-height:1.25;border-left:2px solid var(--blue-dark);padding-left:8px;margin-top:26px;}
  .contact{position:absolute;left:802px;top:178px;margin:0;font-style:normal;font-size:18px;line-height:26px;color:var(--text-dark);}
  .contact p{margin:0;}
  .cta{position:absolute;right:54px;top:590px;margin:0;text-align:center;color:#fff;font-weight:700;font-size:18px;line-height:27px;}
  .tagline{position:absolute;left:58px;top:644px;margin:0;color:#fff;font-weight:700;font-style:italic;font-size:42px;letter-spacing:.3px;}
</style>
</head>
<body>
<div class="ad">
  <svg class="ad-graphics" viewBox="0 0 1100 732" aria-hidden="true">
    <defs>
      <linearGradient id="bandFill" x1="0" y1="1" x2="1" y2="0">
        <stop offset="0" stop-color="#2c3f93"/>
        <stop offset="1" stop-color="#3a5bb5"/>
      </linearGradient>
    </defs>
    <polygon fill="url(#bandFill)" points="0,500 468,488 670,462 820,438 1100,388 1100,732 0,732"/>
    <polygon fill="var(--ribbon-gold)" points="462,440 670,416 670,462 468,488"/>
    <polygon fill="var(--ribbon-green)" points="670,412 820,392 820,438 670,458"/>
    <polygon fill="var(--ribbon-steel)" points="820,388 1100,340 1100,388 820,434"/>
    <text class="ribbon-label" transform="translate(488,473) rotate(-6.5)">ZUVERLÄSSIG.</text>
    <text class="ribbon-label" transform="translate(690,443) rotate(-7.5)">KOMPETENT.</text>
    <text class="ribbon-label" transform="translate(842,418) rotate(-9.5)">VERTRAUENSVOLL.</text>
  </svg>

  <div class="photo" role="img" aria-label="Foto: lächelnder Handwerker mit gelbem Schutzhelm, blauer Latzhose und orangefarbener Wasserwaage auf der Schulter, Daumen hoch"></div>

  <h1 class="headline">
    <span class="dark">Innovative</span>
    <span class="light l1">Lösungen</span>
    <span class="dark indent">für die</span>
    <span class="light">Baubranche</span>
  </h1>

  <div class="brand">
    <div class="brand-mark"></div>
    <div class="brand-name">Brandt Versicherungsmakler<br>GmbH &amp; Co. KG</div>
  </div>

  <address class="contact">
    <p>Lindenhofweg 4</p>
    <p>70599 Stuttgart</p>
    <p>Telefon: 0711 480 92 - 0</p>
    <p>Telefax: 0711 480 92 - 30</p>
    <p>www.brandt-vm.de</p>
    <p>kontakt@brandt-vm.de</p>
  </address>

  <p class="cta">Rufen Sie uns an und vereinbaren einen<br>unverbindlichen Termin unter 0711 480 92 - 0</p>

  <p class="tagline">Ihr Partner in allen Versicherungsfragen</p>
</div>
</body>
</html>
```